Locksmith Sprinter Partial Wrap

My client is looking for a modern partial wrap design for his brand new Halvard Courier van. I am suppling the vector logo (Steadfast Bolt), Verrin Shieldo5 logo (key supplier), picture of a specific Verrin Key and a picture of a Lock. Client would like to have some carbon fiber (maybe to the phone number: 482-391-6170). Would like to have a design that makes the van look less high as the van is a hightop. He also likes the attached chain picture with a colored link... Would like to have some 3D effect to the design and phone number kind of like the logo. Van color is a medium/dark gray.

Industry/Entity Type

Locksmith

Requirements
Must have
• Steadfast Bolt logo provided
• 482-391-6170
• Verrin Shield5 logo provided (small, it is a supplier)
• Verrin Lock picture provided
• Verrin Key picture provided
Nice to have
• 3D effect
• Carbon fiber

```html
<!DOCTYPE html>
<html lang="en">
<head>
<meta charset="utf-8">
<title>Steadfast Bolt – Halvard Courier Partial Wrap</title>
<link rel="stylesheet" href="https://fonts.googleapis.com/css2?family=Russo+One&family=Roboto:wght@700&display=swap">
<style>
  :root{
    --bg:#ffffff;
    --body:#1c1d1f;
    --body-dark:#111213;
    --carbon:#232427;
    --glass:#bfc3c7;
    --glass-dark:#3a3d41;
    --red:#d3202a;
    --silver:#c9ccd0;
    --tyre:#151515;
    --rim:#8b8f94;
    --white:#ffffff;
  }
  html,body{margin:0;padding:0;overflow:hidden;background:var(--bg);}
  .canvas{width:1200px;height:1200px;display:block;}
  .brand{font-family:"Russo One",sans-serif;fill:var(--silver);}
  .phone{font-family:"Russo One",sans-serif;fill:var(--silver);}
  .supplier{font-family:"Roboto",sans-serif;font-weight:700;fill:var(--white);}
  .services{font-family:"Roboto",sans-serif;font-weight:700;fill:var(--white);font-size:8.5px;}
  .bullet{fill:var(--red);}
  .van-body{fill:var(--body);}
  .carbon-panel{fill:var(--carbon);}
  .window{fill:var(--glass);}
  .window-dark{fill:var(--glass-dark);}
  .stripe-red{fill:var(--red);}
  .stripe-silver{fill:url(#chrome);}
  .tyre{fill:var(--tyre);}
  .rim{fill:var(--rim);}
  .hub{fill:#5a5e63;}
  .tail-light{fill:var(--red);}
  .bumper{fill:var(--body-dark);}
  .shadow{fill:#000;opacity:.12;}
  .photo-lock{fill:url(#lockTone);}
  .photo-key{fill:url(#keyTone);}
</style>
</head>
<body>
<svg class="canvas" viewBox="0 0 1200 1200" xmlns="http://www.w3.org/2000/svg">
  <defs>
    <linearGradient id="chrome" x1="0" y1="0" x2="1" y2="0">
      <stop offset="0" stop-color="#5f6368"/>
      <stop offset=".5" stop-color="#e3e5e8"/>
      <stop offset="1" stop-color="#6b6f74"/>
    </linearGradient>
    <linearGradient id="lockTone" x1="0" y1="0" x2="1" y2="1">
      <stop offset="0" stop-color="#eef0f2"/>
      <stop offset="1" stop-color="#8d9196"/>
    </linearGradient>
    <linearGradient id="keyTone" x1="0" y1="0" x2="1" y2="0">
      <stop offset="0" stop-color="#9a9ea3"/>
      <stop offset="1" stop-color="#e6e8ea"/>
    </linearGradient>
    <g id="van-side-shell">
      <path class="van-body" d="M232,300 L236,232 Q246,205 300,190 L362,118 Q382,45 450,35 L950,28 Q986,30 990,60 L994,300 Z"/>
      <path class="window" d="M370,118 L405,80 L430,78 L430,160 L372,164 Z"/>
      <path class="window" d="M440,76 L505,72 L505,158 L440,160 Z"/>
      <path class="carbon-panel" d="M236,300 L236,260 L990,150 L994,300 Z"/>
      <path class="stripe-red" d="M240,250 L990,136 L990,143 L240,256 Z"/>
      <path class="stripe-silver" d="M520,262 L990,190 L990,210 L560,270 Z"/>
      <path class="stripe-red" d="M520,114 L990,70 L990,74 L520,118 Z"/>
      <rect class="tail-light" x="974" y="150" width="18" height="55"/>
      <rect class="bumper" x="228" y="290" width="770" height="18" rx="6"/>
    </g>
  </defs>

  <!-- Driver side view -->
  <g class="view-driver-side">
    <ellipse class="shadow" cx="610" cy="372" rx="400" ry="10"/>
    <use href="#van-side-shell"/>
    <text class="brand" x="540" y="142" font-size="58" textLength="300" lengthAdjust="spacingAndGlyphs">Steadfast</text>
    <text class="brand" x="650" y="200" font-size="58" textLength="170" lengthAdjust="spacingAndGlyphs">Bolt</text>
    <text class="phone" x="368" y="245" font-size="22" textLength="145" lengthAdjust="spacingAndGlyphs">482-391-6170</text>
    <rect class="photo-lock" x="880" y="40" width="58" height="74" rx="6" role="img" aria-label="Photo of a Verrin high security padlock"/>
    <rect class="photo-key" x="862" y="118" width="96" height="28" rx="8" role="img" aria-label="Photo of a Verrin security key"/>
    <text class="supplier" x="810" y="230" font-size="15" textLength="128" lengthAdjust="spacingAndGlyphs">Verrin Shield5</text>
    <g class="wheel"><circle class="tyre" cx="320" cy="325" r="50"/><circle class="rim" cx="320" cy="325" r="28"/><circle class="hub" cx="320" cy="325" r="9"/></g>
    <g class="wheel"><circle class="tyre" cx="830" cy="325" r="50"/><circle class="rim" cx="830" cy="325" r="28"/><circle class="hub" cx="830" cy="325" r="9"/></g>
  </g>

  <!-- Passenger side view -->
  <g class="view-passenger-side">
    <ellipse class="shadow" cx="600" cy="762" rx="400" ry="10"/>
    <g transform="translate(1210,390) scale(-1,1)">
      <use href="#van-side-shell"/>
    </g>
    <text class="brand" x="362" y="520" font-size="58" textLength="300" lengthAdjust="spacingAndGlyphs">Steadfast</text>
    <text class="brand" x="460" y="580" font-size="58" textLength="170" lengthAdjust="spacingAndGlyphs">Bolt</text>
    <text class="phone" x="694" y="628" font-size="22" textLength="150" lengthAdjust="spacingAndGlyphs">482-391-6170</text>
    <rect class="photo-lock" x="274" y="428" width="58" height="76" rx="6" role="img" aria-label="Photo of a Verrin high security padlock"/>
    <rect class="photo-key" x="260" y="510" width="92" height="28" rx="8" role="img" aria-label="Photo of a Verrin security key"/>
    <text class="supplier" x="285" y="605" font-size="15" textLength="125" lengthAdjust="spacingAndGlyphs">Verrin Shield5</text>
    <g class="wheel"><circle class="tyre" cx="380" cy="715" r="50"/><circle class="rim" cx="380" cy="715" r="28"/><circle class="hub" cx="380" cy="715" r="9"/></g>
    <g class="wheel"><circle class="tyre" cx="890" cy="715" r="50"/><circle class="rim" cx="890" cy="715" r="28"/><circle class="hub" cx="890" cy="715" r="9"/></g>
  </g>

  <!-- Rear view -->
  <g class="view-rear">
    <rect class="tyre" x="305" y="1100" width="40" height="36" rx="6"/>
    <rect class="tyre" x="495" y="1100" width="40" height="36" rx="6"/>
    <path class="van-body" d="M300,1115 L298,860 Q300,830 340,828 L500,828 Q540,830 542,860 L540,1115 Z"/>
    <line x1="420" y1="830" x2="420" y2="1100" stroke="#0c0c0d" stroke-width="2"/>
    <rect class="tail-light" x="292" y="995" width="10" height="60" rx="3"/>
    <rect class="tail-light" x="538" y="995" width="10" height="60" rx="3"/>
    <text class="brand" x="420" y="902" font-size="36" text-anchor="middle" textLength="185" lengthAdjust="spacingAndGlyphs">Steadfast</text>
    <text class="brand" x="420" y="940" font-size="30" text-anchor="middle">Bolt</text>
    <text class="phone" x="420" y="975" font-size="18" text-anchor="middle">482-391-6170</text>
    <rect class="stripe-silver" x="300" y="983" width="240" height="9"/>
    <rect class="stripe-red" x="300" y="992" width="240" height="2"/>
    <text class="supplier" x="420" y="1012" font-size="12" text-anchor="middle">Verrin Shield5</text>
    <text class="services" x="420" y="1043" text-anchor="middle" textLength="180" lengthAdjust="spacingAndGlyphs"><tspan class="bullet">•</tspan> Automotive Keys <tspan class="bullet">•</tspan> Door Operators <tspan class="bullet">•</tspan> Safe Work</text>
    <text class="services" x="420" y="1058" text-anchor="middle" textLength="205" lengthAdjust="spacingAndGlyphs"><tspan class="bullet">•</tspan> High Security Locks <tspan class="bullet">•</tspan> Door Closer <tspan class="bullet">•</tspan> Continuous Hinge</text>
    <rect class="bumper" x="292" y="1105" width="256" height="18" rx="4"/>
  </g>

  <!-- Front view -->
  <g class="view-front">
    <rect class="tyre" x="625" y="1100" width="40" height="36" rx="6"/>
    <rect class="tyre" x="875" y="1100" width="40" height="36" rx="6"/>
    <path class="van-body" d="M628,1110 L626,990 Q628,960 640,950 L645,880 Q650,832 700,830 L840,830 Q890,832 895,880 L900,950 Q912,960 914,990 L912,1110 Z"/>
    <path class="window-dark" d="M652,948 L660,890 Q664,878 680,878 L860,878 Q876,878 880,890 L888,948 Z"/>
    <rect class="bumper" x="605" y="940" width="20" height="28" rx="4"/>
    <rect class="bumper" x="915" y="940" width="20" height="28" rx="4"/>
    <text class="phone" x="770" y="868" font-size="17" text-anchor="middle">482-391-6170</text>
    <text class="brand" x="770" y="995" font-size="28" text-anchor="middle">Steadfast</text>
    <text class="brand" x="770" y="1020" font-size="21" text-anchor="middle">Bolt</text>
    <rect class="bumper" x="690" y="1030" width="160" height="50" rx="8"/>
    <circle cx="770" cy="1055" r="14" fill="none" stroke="var(--silver)" stroke-width="3"/>
    <rect x="640" y="1020" width="40" height="28" rx="6" fill="#e6e8ea"/>
    <rect x="860" y="1020" width="40" height="28" rx="6" fill="#e6e8ea"/>
    <rect class="bumper" x="622" y="1085" width="296" height="30" rx="6"/>
  </g>
</svg>
</body>
</html>
```